Australian Real Estate Sales Consultant needs web design please.

I am a female residential real estate sales consultant for a large australian real estate franchise.
I need a web design for "wordpress" that contains an area that will accommodate my photo and details and company logo.
A large area that contains a feature property where images are on something like a slide show.
Tabs or something similar with images for Selling, Sold, Photography and News where people can look at listings but I do not want people to be able to post a comment.
Reason: Need more designers, may be forced to change to wordpress and offer more money.
Reason: Sorry for the delay, I have been concentrating on another project which I needed completed. I am now able to focus on my web design project and hope to have it all set up in the next 10 days as it is a high priority for me. Thank you for your patience and I will begin providing feedback to your designs shortly. Thanks, Marisha.
Target Market(s)
Potential sellers or purchasers of residential property
Industry/Entity Type
Residential
Requirements
Must have
- Ease of changing property photos and info
Nice to have
- Bright attractive colours

```html
<!DOCTYPE html>
<html lang="en">
<head>
<meta charset="utf-8">
<title>Harbourline Realty — Residential Sales Consultant</title>
<link href="https://fonts.googleapis.com/css2?family=Source+Sans+3:wght@400;600;700&family=Open+Sans:wght@400;600;700&display=swap" rel="stylesheet">
<style>
  :root{
    --red:#e02a2a;
    --red-dark:#b8131b;
    --blue:#1167ad;
    --ink:#333333;
    --text:#4a4a4a;
    --muted:#a8a8a8;
    --rule:#d8d8d8;
    --panel:#f5f5f5;
    --footer:#353535;
    --sky:#cfe0ea;
  }
  *{margin:0;padding:0;box-sizing:border-box}
  html,body{width:1200px;height:1038px;overflow:hidden}
  body{
    position:relative;
    background:linear-gradient(180deg,var(--sky) 0,#e8f0f5 300px,#fff 620px);
    font-family:"Open Sans",Arial,sans-serif;
    color:var(--text);
  }
  .page{
    position:absolute;left:116px;top:0;width:966px;height:1038px;
    background:#fff;box-shadow:0 0 40px rgba(120,150,170,.35);
  }
  .abs{position:absolute}
  /* header */
  .site-header{left:0;top:0;width:966px;height:99px;background:linear-gradient(#f6f6f6,#fff 40px)}
  .brand{left:22px;top:31px;display:flex;align-items:center;gap:10px;
    font-family:"Source Sans 3",sans-serif;font-weight:700;font-size:27px;line-height:34px;color:var(--red)}
  .brand-mark{width:22px;height:22px;background:var(--red)}
  .main-nav{left:0;top:51px;font-size:12px;color:var(--ink)}
  .main-nav a{position:absolute;white-space:nowrap;color:inherit;text-decoration:none}
  .main-nav a.is-active{color:var(--red-dark)}
  /* hero */
  .hero{left:1px;top:99px;width:964px;height:332px;
    background:linear-gradient(90deg,#b59a78 0,#8c7258 55%,#6a4a3a 100%)}
  .hero-panel{left:1px;top:192px;width:504px;height:223px;background:rgba(70,62,55,.72);color:#fff}
  .hero-panel h1{position:absolute;left:20px;top:22px;width:400px;
    font-family:"Source Sans 3",sans-serif;font-weight:400;font-size:30px;line-height:32px;letter-spacing:-.3px}
  .hero-panel p{position:absolute;left:20px;top:97px;width:460px;font-size:11px;line-height:15.5px}
  .btn{position:absolute;left:20px;top:171px;width:106px;height:26px;border-radius:4px;
    background:linear-gradient(#f0453c,#c81c1c);color:#fff;font-family:"Source Sans 3",sans-serif;
    font-weight:700;font-size:13px;line-height:26px;padding-left:14px;box-shadow:0 1px 2px rgba(0,0,0,.4)}
  .btn svg{position:absolute;right:14px;top:9px}
  /* columns */
  .col-title{font-family:"Source Sans 3",sans-serif;font-weight:600;font-size:19px;line-height:24px;color:var(--ink);
    padding-bottom:11px;border-bottom:1px solid var(--rule)}
  .listing{width:280px}
  .photo-frame{position:relative;margin-top:11px;height:134px;background:#fff;
    box-shadow:0 1px 5px rgba(0,0,0,.25);padding:6px 5px}
  .photo{width:100%;height:121px}
  .photo.house-blue{background:#5a7596}
  .photo.house-green{background:linear-gradient(#8fb6dc,#7fa35c)}
  .ribbon{position:absolute;right:-4px;top:-5px}
  .listing h3{margin-top:17px;font-size:12px;line-height:17px;font-weight:700;color:var(--ink)}
  .listing p,.news p{font-size:11.2px;line-height:15.5px;margin-top:2px}
  .more{color:var(--red-dark);text-decoration:underline}
  .spec{margin-top:8px;list-style:none;font-size:11.2px;font-weight:700;color:var(--ink)}
  .spec li{line-height:16px;padding-left:12px;position:relative}
  .spec li:before{content:"";position:absolute;left:2px;top:5px;border-left:4px solid var(--red-dark);
    border-top:3px solid transparent;border-bottom:3px solid transparent}
  .contact-box{left:19px;top:783px;width:598px;height:90px;background:var(--panel);
    padding:21px 30px 21px 16px;font-family:"Source Sans 3",sans-serif;font-size:18px;line-height:22px;color:var(--ink)}
  .contact-box span{color:var(--red)}
  /* sidebar */
  .news{width:283px}
  .entry{margin-top:11px}
  .entry+.entry{margin-top:16px}
  .date{font-size:9.5px;color:var(--muted);line-height:12px}
  .entry h4{font-size:12px;font-weight:600;color:var(--ink);line-height:14px}
  .entry h4.hl{color:var(--red-dark)}
  .news p{margin-top:1px}
  .side-title{margin-top:26px}
  .quote{margin-top:14px}
  .quote+.quote{margin-top:10px}
  .quote p{margin-top:0}
  .author{font-size:11px;font-weight:700;color:var(--ink);margin-top:3px;line-height:15px}
  .author span{color:var(--red-dark)}
  /* footer */
  .site-footer{left:0;top:909px;width:966px;height:129px;background:var(--footer);
    color:#fff;font-size:11px;text-align:center;padding-top:60px}
  .site-footer:before{content:"";position:absolute;left:0;top:0;width:100%;height:30px;
    background:radial-gradient(ellipse at 50% 0,rgba(0,0,0,.45),transparent 70%)}
</style>
</head>
<body>
<div class="page">
  <header class="site-header abs">
    <div class="brand abs"><span class="brand-mark"></span>Harbourline Realty</div>
    <nav class="main-nav abs">
      <a class="is-active" style="left:493px">HOME</a>
      <a style="left:560px">ABOUT US</a>
      <a style="left:652px">RESIDENTAL</a>
      <a style="left:752px">REAL ESTATE</a>
      <a style="left:861px">CONTACT US</a>
    </nav>
  </header>

  <section class="hero abs" role="img" aria-label="Portrait photo of the sales consultant on a house verandah"></section>
  <div class="hero-panel abs">
    <h1>I am a female residential real estate sales consultant</h1>
    <p>Lorem ipsum dolor sit amet, consectetur adipisicing elit, sed do eiusmod tempor incididunt ut labore et dolore magna aliqua. Ut enim ad minim veniam, quis nostrud exercitation ullamco laboris nisi ut aliquip ex ea commodo consequat.</p>
    <div class="btn">Readmore<svg width="6" height="8"><path d="M0 0L6 4L0 8Z" fill="#fff"/></svg></div>
  </div>

  <section class="listing abs" style="left:19px;top:450px">
    <h2 class="col-title">Selling</h2>
    <div class="photo-frame">
      <div class="photo house-blue" role="img" aria-label="Photo of a two-storey family house for sale"></div>
      <svg class="ribbon" width="110" height="80" viewBox="0 0 110 80"><path d="M26 0H60L110 50V84Z" fill="#e82020"/><text transform="translate(58 30) rotate(43)" fill="#fff" font-family="Source Sans 3,sans-serif" font-size="15" font-weight="600">Sell</text></svg>
    </div>
    <h3>Real Estate Type</h3>
    <p>Lorem ipsum dolor sit amet, consectetur adipisicing elit, sed do eiusmod tempor incididunt ut labore et dolore magna aliqua. <span class="more">Readmore</span></p>
    <ul class="spec"><li>Real Estate Type Small 125</li><li>Real Estate Type Medium 125</li></ul>
  </section>

  <section class="listing abs" style="left:339px;top:450px">
    <h2 class="col-title">Sold</h2>
    <div class="photo-frame">
      <div class="photo house-green" role="img" aria-label="Photo of a sold country house with gardens"></div>
      <svg class="ribbon" width="110" height="80" viewBox="0 0 110 80"><path d="M26 0H60L110 50V84Z" fill="#1167ad"/><text transform="translate(44 22) rotate(43)" fill="#fff" font-family="Source Sans 3,sans-serif" font-size="15" font-weight="600">Sold Out</text></svg>
    </div>
    <h3>Real Estate Type</h3>
    <p>Lorem ipsum dolor sit amet, consectetur adipisicing elit, sed do eiusmod tempor incididunt ut labore et dolore magna aliqua. <span class="more">Readmore</span></p>
    <ul class="spec"><li>Real Estate Type Small 125</li><li>Real Estate Type Medium 125</li></ul>
  </section>

  <div class="contact-box abs">if you want to consult about the residential real estate, please contact me at <span>hello@harbourlinerealty.com</span> or <span>088-5550142</span></div>

  <aside class="news abs" style="left:656px;top:450px">
    <h2 class="col-title">News</h2>
    <div class="entry"><div class="date">October 10, 2011</div><h4 class="hl">Lorem Ipsum</h4><p>Lorem ipsum dolor sit amet, consectetur adipisicing elit, sed do eiusmod tempor incididunt ut labore et dolore magna aliqua.</p></div>
    <div class="entry"><div class="date">October 10, 2011</div><h4>Lorem Ipsum</h4><p>Lorem ipsum dolor sit amet, consectetur adipisicing elit, sed do eiusmod tempor incididunt ut labore et dolore magna aliqua.</p></div>
    <h2 class="col-title side-title">Testimonials</h2>
    <div class="quote"><div class="date">October 10, 2011</div><p>Lorem ipsum dolor sit amet, consectetur adipisicing elit, sed do eiusmod tempor.</p><div class="author">Tom Rennick - <span>Sidney</span></div></div>
    <div class="quote"><div class="date">October 10, 2011</div><p>Lorem ipsum dolor sit amet, consectetur adipisicing elit, sed do eiusmod tempor.</p><div class="author">Alan Whitby - <span>Melbourne</span></div></div>
  </aside>

  <footer class="site-footer abs">Copyright © 2011 harbourlinerealty.&nbsp; User Agreement and Privacy Policy.</footer>
</div>
</body>
</html>
```